PREMIUM AGENCY High End Business Card - A+++ Designers Wanted

** DO NOT ATTEMPT TO CONTACT ME THROUGH SEARCHING ON ZINTREL OR EMAILING ME THROUGH MY WEBSITE **

I need a fresh, contemporary business card designed using the logo attached (BRONSALK)

I have attached the font for BRONSALK

It must have a premium look and feel. The business card size must be STANDARD size.

You can submit either/both VERTICAL or HORIZONTAL designs.

FRONT: It must have the following sample information on

Paul Ardley
Director Operations
Mobile +61 452 118 906
Email paulardley@bronsalk.com
www.bronsalk.com

The REAR of the business card must have the words

CREATE INSPIRE TOMORROW

as part of the design, in the same font (NEXA) attached.

The words do not need to be in capitals, or on the same line, please design this as you see it best working.

ADDITIONAL INFORMATION
======================

The BRONSALK logo must be on the front of the card

I want Ultraviolet printing on the final design, to enhance either the NAME of the person OR the BRONSALK logo OR the words on the back of the card.

Target Market(s)

Agency, Advertising Agency, Creative, Designers

Industry/Entity Type

Media

Contact Information for Business Card

Design Agency, Contemporary, Premium look and feel, High Quality

Font styles to use
Serif
Sans Serif
Other font styles liked:
• ATTACHED TO PROJECT

Requirements
Must have
• BLACK & WHITE as the primary design, and if you feel there can be a highlighted colour, then this can be used.
• The Logo ICON attached is blue, this colour must not be changed.
• I have attached the partner brand BRONSALK MEDIA incase you need to manipulate the original files.
• ** DO NOT ATTEMPT TO CONTACT ME THROUGH SEARCHING ON ZINTREL OR EMAILING ME THROUGH MY WEBSITE **
Nice to have
• Must be Premium. I have attached some sample designs, that I like that would be a good inspiration for where this can be taken.
• My favourite design is is the KESTRAVUE2-BUSINESSCARD-TEMPLATE
Should not have
• No funny or silly standard / off the shelf designs

```html
<!DOCTYPE html>
<html lang="en">
<head>
<meta charset="utf-8">
<title>Bronsalk Business Cards</title>
<link rel="stylesheet" href="https://fonts.googleapis.com/css2?family=Montserrat:wght@500;600;700&family=Questrial&display=swap">
<style>
  :root {
    --page: #e6e7e8;
    --card: #231f20;
    --ink-deep: #0a090c;
    --brand-blue: #29a9e1;
    --white: #ffffff;
    --soft-white: #f1f1f1;
    --name-grey: #8f8f8f;
    --title-grey: #8a8a8a;
    --rule: #050505;
  }
  * { margin: 0; padding: 0; box-sizing: border-box; }
  html, body { width: 1200px; height: 2951px; overflow: hidden; background: var(--page); }
  body { position: relative; font-family: "Questrial", sans-serif; }

  .card {
    position: absolute;
    left: 106px;
    width: 988px;
    height: 604px;
    background: var(--card);
    overflow: hidden;
  }
  .card--rounded { border-radius: 56px; }
  .card--back-square { top: 106px; }
  .card--front-square { top: 816px; }
  .card--back-rounded { top: 1528px; }
  .card--front-rounded { top: 2240px; }

  .brand-mark-area {
    position: absolute;
    left: -410px;
    top: -58px;
    width: 720px;
    height: 720px;
  }

  .tagline {
    font-family: "Montserrat", sans-serif;
    font-weight: 600;
    color: var(--ink-deep);
  }
  .tagline__line {
    position: absolute;
    left: 356px;
    display: block;
    white-space: nowrap;
    line-height: 1;
  }
  .tagline__line--create { top: 177px; font-size: 78px; letter-spacing: 51px; }
  .tagline__line--inspire { top: 246px; font-size: 140px; letter-spacing: 18px; }
  .tagline__line--tomorrow { top: 373px; font-size: 84px; letter-spacing: 3px; }

  .back-url {
    position: absolute;
    left: 432px;
    top: 516px;
    font-size: 26px;
    letter-spacing: 12px;
    color: var(--soft-white);
  }
  .back-url strong { font-family: "Montserrat", sans-serif; font-weight: 700; }

  .brand {
    position: absolute;
    left: 362px;
    top: 70px;
    display: flex;
    align-items: center;
    gap: 36px;
  }
  .brand__dot {
    width: 54px;
    height: 54px;
    border-radius: 50%;
    background: var(--brand-blue);
  }
  .brand__name {
    font-family: "Montserrat", sans-serif;
    font-weight: 600;
    font-size: 76px;
    letter-spacing: 4px;
    color: var(--white);
    line-height: 1;
  }

  .person {
    position: absolute;
    left: 358px;
    top: 280px;
    color: var(--name-grey);
  }
  .person__name { font-size: 86px; line-height: 1; letter-spacing: 1px; }
  .person__surname { font-size: 56px; letter-spacing: 1px; }
  .person__title { font-size: 28px; letter-spacing: 2px; color: var(--title-grey); margin-top: 4px; }

  .divider {
    position: absolute;
    left: 358px;
    right: 0;
    top: 420px;
    height: 5px;
    background: var(--rule);
  }

  .contact {
    position: absolute;
    left: 358px;
    top: 450px;
    list-style: none;
    color: var(--soft-white);
    font-size: 28px;
    letter-spacing: 1px;
    line-height: 38px;
  }
  .contact--with-icons li { display: flex; align-items: center; gap: 22px; }
  .contact__icon { width: 24px; height: 24px; flex: none; }
</style>
</head>
<body>

  <section class="card card--back-square">
    <svg class="brand-mark-area" viewBox="0 0 720 720" role="img" aria-label="Large Bronsalk brand mark decoration">
      <circle cx="360" cy="360" r="340" fill="#0a090c"/>
    </svg>
    <h2 class="tagline">
      <span class="tagline__line tagline__line--create">CREATE</span>
      <span class="tagline__line tagline__line--inspire">INSPIR</span>
      <span class="tagline__line tagline__line--tomorrow">TOMORROW</span>
    </h2>
    <p class="back-url">www.<strong>bronsalk</strong>.com</p>
  </section>

  <section class="card card--front-square">
    <svg class="brand-mark-area" viewBox="0 0 720 720" role="img" aria-label="Large Bronsalk brand mark decoration">
      <circle cx="360" cy="360" r="340" fill="#0a090c"/>
    </svg>
    <div class="brand"><span class="brand__dot"></span><span class="brand__name">BRONSALK</span></div>
    <div class="person">
      <p class="person__name">PAUL <span class="person__surname">ARDLEY</span></p>
      <p class="person__title">Director Operations</p>
    </div>
    <div class="divider"></div>
    <ul class="contact">
      <li>+61 452 118 906</li>
      <li>paulardley@bronsalk.com</li>
      <li>www.bronsalk.com</li>
    </ul>
  </section>

  <section class="card card--rounded card--back-rounded">
    <svg class="brand-mark-area" viewBox="0 0 720 720" role="img" aria-label="Large blue Bronsalk brand mark decoration">
      <circle cx="360" cy="360" r="340" fill="#29a9e1"/>
    </svg>
    <h2 class="tagline">
      <span class="tagline__line tagline__line--create">CREATE</span>
      <span class="tagline__line tagline__line--inspire">INSPIR</span>
      <span class="tagline__line tagline__line--tomorrow">TOMORROW</span>
    </h2>
    <p class="back-url">www.<strong>bronsalk</strong>.com</p>
  </section>

  <section class="card card--rounded card--front-rounded">
    <svg class="brand-mark-area" viewBox="0 0 720 720" role="img" aria-label="Large Bronsalk brand mark decoration">
      <circle cx="360" cy="360" r="340" fill="#0a090c"/>
    </svg>
    <div class="brand"><span class="brand__dot"></span><span class="brand__name">BRONSALK</span></div>
    <div class="person">
      <p class="person__name">PAUL <span class="person__surname">ARDLEY</span></p>
      <p class="person__title">Director Operations</p>
    </div>
    <div class="divider"></div>
    <ul class="contact contact--with-icons">
      <li>
        <svg class="contact__icon" viewBox="0 0 24 24" aria-hidden="true"><rect x="6" y="1" width="12" height="22" rx="2" fill="none" stroke="#29a9e1" stroke-width="2.5"/><rect x="10" y="18" width="4" height="2" fill="#29a9e1"/></svg>
        +61 452 118 906
      </li>
      <li>
        <svg class="contact__icon" viewBox="0 0 24 24" aria-hidden="true"><rect x="1" y="5" width="22" height="15" fill="#29a9e1"/><path d="M1 5 L12 14 L23 5" fill="none" stroke="#231f20" stroke-width="2"/></svg>
        paulardley@bronsalk.com
      </li>
      <li>
        <svg class="contact__icon" viewBox="0 0 24 24" aria-hidden="true"><path d="M14 3 L23 11 L14 19 V14 C8 14 4 16 1 21 C2 13 6 8 14 8 Z" fill="#29a9e1"/></svg>
        www.bronsalk.com
      </li>
    </ul>
  </section>

</body>
</html>
```